Logo & Visitenkarte für Hochzeitsplanerin
Zielgruppe
Mein Name ist Carola Wendt und ich bin Hochzeitsplanerin mit BVR Zertigfikat. Ich komme aus Köln und möchte als selbstständige Hochzeitsplanerin vor allem kölsche Hochzeiten und Hochzeiten mit Lumora Elementen anbieten. Meine Zielgruppe sind junge Brautpaare bis mitte/ende 30 welche genauso heimatverbunden sind wie ich.
Aufgabenstellung
Die Farben rosa und Bordeaux sollen vorkommen und es sollte ein wenig verspielt sein, jedoch nicht zu kindisch. Bitte auf der Visitenkarte noch Hochzeitsplanerin Carola Wendt (BVR) abbilden.

```html
<!DOCTYPE html>
<html lang="de">
<head>
<meta charset="utf-8">
<title>Ja für immer – Visitenkarte Carola Wendt</title>
<link rel="stylesheet" href="https://fonts.googleapis.com/css2?family=Marcellus&family=Quicksand:wght@500&display=swap">
<style>
  :root {
    --paper: #ffffff;
    --rose: #e9aba8;
    --bordeaux: #7b1b2c;
    --ink: #3b1d22;
    --white: #ffffff;
  }
  * { margin: 0; padding: 0; box-sizing: border-box; }
  html, body {
    width: 1200px;
    height: 786px;
    overflow: hidden;
    background: var(--paper);
  }
  .card {
    position: absolute;
    left: 39px;
    top: 39px;
    width: 1122px;
    height: 700px;
    background: var(--rose);
  }
  .brand-name {
    position: absolute;
    left: 126px;
    top: 112px;
    font-family: "Marcellus", serif;
    font-size: 82px;
    color: var(--white);
    white-space: nowrap;
  }
  .brand-mark {
    position: absolute;
    left: 664px;
    top: 41px;
    width: 300px;
    height: 300px;
  }
  .holder {
    position: absolute;
    left: 247px;
    top: 306px;
    font-family: "Marcellus", serif;
    color: var(--bordeaux);
    text-transform: uppercase;
    line-height: 1.2;
  }
  .holder-name { font-size: 33px; letter-spacing: 1px; }
  .holder-title { font-size: 35px; letter-spacing: 1px; font-weight: 700; }
  .contact {
    position: absolute;
    left: 247px;
    top: 452px;
    list-style: none;
    font-family: "Quicksand", sans-serif;
    font-weight: 500;
    font-size: 29px;
    color: var(--ink);
    line-height: 36px;
  }
  .contact li { display: flex; align-items: center; gap: 8px; }
  .contact-icon { width: 26px; height: 26px; flex: none; }
  .social-square {
    width: 22px;
    height: 22px;
    background: var(--ink);
    flex: none;
  }
</style>
</head>
<body>
  <section class="card">
    <div class="brand-name">Ja für immer</div>
    <svg class="brand-mark" viewBox="0 0 300 300" aria-hidden="true">
      <circle cx="150" cy="150" r="145" fill="none" stroke="var(--bordeaux)" stroke-width="4"/>
    </svg>

    <div class="holder">
      <p class="holder-name">Carola Wendt</p>
      <p class="holder-title">Hochzeitsplanerin BVR</p>
    </div>

    <ul class="contact">
      <li>www.jafuerimmer.de</li>
      <li>carola@jafuerimmer.de</li>
      <li>
        <svg class="contact-icon" viewBox="0 0 24 24" aria-label="Telefon">
          <path fill="var(--ink)" d="M6.6 10.8a15.1 15.1 0 0 0 6.6 6.6l2.2-2.2c.3-.3.7-.4 1-.2 1.1.4 2.3.6 3.6.6.6 0 1 .4 1 1V20c0 .6-.4 1-1 1A17 17 0 0 1 3 4c0-.6.4-1 1-1h3.5c.6 0 1 .4 1 1 0 1.3.2 2.5.6 3.6.1.3 0 .7-.2 1z"/>
        </svg>
        +49 (0)221 40377615
      </li>
      <li><span class="social-square"></span>@jafuerimmer</li>
    </ul>
  </section>
</body>
</html>
```